Letterhead for SaaS

Design a letterhead that aligns with our new business card, using our logo and color scheme and text defined in the Branding Guide to ensure consistency. Consider incorporating a subtle watermark for added elegance. The layout should reflect the card's style, creating a cohesive look across our stationery.

```html
<!DOCTYPE html>
<html lang="en">
<head>
<meta charset="utf-8">
<title>Velmora Letterhead</title>
<link rel="stylesheet" href="https://fonts.googleapis.com/css2?family=Montserrat:wght@800&family=Lato:wght@400;700&family=Dancing+Script:wght@600&display=swap">
<style>
  :root {
    --backdrop: #e4e5e7;
    --paper: #ffffff;
    --navy: #121a2b;
    --sky: #3bbbec;
    --ink: #1d1f24;
    --muted: #3a3d44;
    --watermark: #ececec;
  }
  * { box-sizing: border-box; margin: 0; padding: 0; }
  html, body { width: 1200px; height: 960px; overflow: hidden; }
  body {
    background: var(--backdrop);
    font-family: "Lato", Arial, sans-serif;
    color: var(--ink);
    position: relative;
  }
  .letterhead {
    position: absolute;
    left: 282px; top: 30px;
    width: 636px; height: 900px;
    background: var(--paper);
    box-shadow: 0 4px 18px rgba(0,0,0,.12);
    overflow: hidden;
  }
  .brand {
    position: absolute; left: 48px; top: 62px;
    display: flex; align-items: center; gap: 12px;
  }
  .brand-dot { width: 34px; height: 34px; border-radius: 50%; background: var(--navy); }
  .brand-name {
    font-family: "Montserrat", Arial, sans-serif;
    font-weight: 800; font-size: 30px; letter-spacing: 1px; color: var(--navy);
  }
  .header-rule {
    position: absolute; left: 48px; right: 40px; top: 128px;
    height: 1px; background: var(--sky);
  }
  .contact-tick {
    position: absolute; left: 372px; top: 96px;
    width: 1px; height: 26px; background: var(--sky);
  }
  .contact-list {
    position: absolute; left: 388px; top: 60px;
    list-style: none; font-size: 10.5px; color: var(--muted); line-height: 15px;
  }
  .contact-list li { display: flex; align-items: center; gap: 6px; }
  .contact-list svg { width: 9px; height: 9px; fill: var(--sky); }
  .watermark {
    position: absolute; left: 250px; top: 210px;
    width: 300px; height: 300px;
    background: radial-gradient(circle, var(--watermark) 0%, rgba(236,236,236,.6) 55%, rgba(255,255,255,0) 72%);
  }
  .letter-body {
    position: absolute; left: 60px; top: 160px; width: 520px;
    font-size: 11px; line-height: 14px; color: var(--muted);
  }
  .date { margin-bottom: 18px; }
  .recipient { margin-bottom: 16px; }
  .address { margin-bottom: 22px; }
  .salutation { font-weight: 700; font-size: 15px; color: var(--ink); margin-bottom: 12px; }
  .letter-body p.para { font-size: 10px; line-height: 13px; margin-bottom: 14px; }
  .closing { margin-top: 28px; }
  .signature {
    position: absolute; left: 120px; top: 760px;
    font-family: "Dancing Script", cursive; font-size: 34px; color: var(--ink);
    transform: rotate(-6deg);
  }
  .footer-wave { position: absolute; left: 0; bottom: 0; width: 636px; height: 900px; pointer-events: none; }
</style>
</head>
<body>
  <main class="letterhead">
    <div class="brand">
      <span class="brand-dot"></span>
      <span class="brand-name">VELMORA</span>
    </div>

    <ul class="contact-list">
      <li><svg viewBox="0 0 10 10"><path d="M2 1 L4 1 L4.5 3.5 L3.3 4.3 Q4.3 6 5.8 6.8 L6.5 5.6 L9 6 L9 8 Q8.5 9 7.5 9 Q1 8 1 2.5 Q1 1.3 2 1Z"/></svg>(555) 014-2290</li>
      <li><svg viewBox="0 0 10 10"><path d="M0.5 2 H9.5 V8 H0.5Z M0.5 2 L5 5.5 L9.5 2" /></svg>dana.r@velmora.com</li>
      <li><svg viewBox="0 0 10 10"><circle cx="5" cy="5" r="4.5"/></svg>www.velmora.com</li>
    </ul>
    <span class="contact-tick"></span>
    <span class="header-rule"></span>

    <div class="watermark" role="img" aria-label="Faint large brand watermark behind the letter text"></div>

    <section class="letter-body">
      <p class="date">January-03-2020</p>
      <p class="recipient">Mr. Alan Reed<br>President</p>
      <p class="address">Harbor Corporation<br>123 Street Name, Suite# 10<br>City, State, 120023</p>
      <p class="salutation">Dear Mr. Reed</p>
      <p class="para">Lorem ipsum dolor sit amet, consectetur adipiscing elit, sed do eiusmod tempor incididunt ut labore et dolore magna aliqua. Ut enim ad minim veniam, quis nostrud exercitation ullamco laboris nisi ut aliquip ex ea commodo consequat. Duis aute irure dolor in reprehenderit in voluptate velit esse cillum dolore eu fugiat nulla pariatur.</p>
      <p class="para">Lorem ipsum dolor sit amet, consectetur adipiscing elit, sed do eiusmod tempor incididunt ut labore et dolore magna aliqua. Ut enim ad minim veniam, quis nostrud exercitation ullamco laboris nisi ut aliquip ex ea commodo consequat. Duis aute irure dolor in reprehenderit in voluptate velit esse cillum dolore eu fugiat nulla pariatur.</p>
      <p class="para">Lorem ipsum dolor sit amet, consectetur adipiscing elit, sed do eiusmod tempor incididunt ut labore et dolore magna aliqua. Ut enim ad minim veniam, quis nostrud exercitation ullamco laboris nisi ut aliquip ex ea commodo consequat.</p>
      <p class="para">Excepteur sint occaecat cupidatat non proident, sunt in culpa qui officia deserunt mollit anim id est laborum. re et dolore magnam aliquam quaerat voluptatem.</p>
      <p class="closing">Regards</p>
    </section>

    <p class="signature">Nora Bell</p>

    <svg class="footer-wave" viewBox="0 0 636 900" aria-hidden="true">
      <path d="M0 866 C 280 856 500 820 636 742 L636 900 L0 900 Z" fill="var(--sky)"/>
      <path d="M0 874 C 282 864 504 830 636 754 L636 900 L0 900 Z" fill="var(--paper)"/>
      <path d="M0 878 C 284 868 508 836 636 760 L636 900 L0 900 Z" fill="var(--navy)"/>
    </svg>
  </main>
</body>
</html>
```